Brookfarrow Osteopathy and dry needling business card

Business card for Brookfarrow Osteopathy and Dry Needling.

Industry/Entity Type

Health

Contact Information for Business Card

I do not have a phone number yet. I also do not have an email address yet. The physical address is: 48 Lower Crane Street Brookfarrow The website is: www.brookfarrowosteosteopathy.example My details are: Dr Martin Pellowe, Osteopath (B.Clin.Sci (Ost) M.Ost BSC ECON (Hons)

Colors
0094D4
00A9DD
6FCCEA
C7EBF8
E9F6FB

Requirements
Must have
• logo on the back
Nice to have
• Maybe a space for me to write an appointment time and date on the card.

```html
<!DOCTYPE html>
<html lang="en">
<head>
<meta charset="utf-8">
<title>Brookfarrow Osteopathy and Dry Needling – Business Card</title>
<link href="https://fonts.googleapis.com/css2?family=Poppins:wght@400;500;600;700&display=swap" rel="stylesheet">
<style>
  :root {
    --stage: #858585;
    --card: #ffffff;
    --brand-blue: #1592d2;
    --brand-orange: #f7941d;
    --ink: #1d1d1d;
    --muted: #9b9b9b;
    --rule: #8a8a8a;
    --pale-blue: #e9f6fb;
    --soft-blue: #c7ebf8;
  }
  * { margin: 0; padding: 0; box-sizing: border-box; }
  html, body {
    width: 960px; height: 1200px; overflow: hidden;
    background: var(--stage);
    font-family: "Poppins", sans-serif;
    color: var(--ink);
  }
  .card {
    position: absolute;
    left: 70px; width: 821px; height: 469px;
    background: var(--card);
    overflow: hidden;
    box-shadow: 14px 14px 28px rgba(0,0,0,0.25);
  }
  .card--front { top: 101px; }
  .card--back { top: 637px; }

  /* Front */
  .person { position: absolute; left: 76px; top: 80px; }
  .person__name {
    font-size: 37px; line-height: 1; letter-spacing: -0.5px;
    white-space: nowrap;
  }
  .person__first { color: var(--brand-blue); font-weight: 700; }
  .person__last { color: var(--brand-orange); font-weight: 400; }
  .person__role {
    margin-top: 11px;
    font-size: 17px; font-weight: 500; letter-spacing: 3.2px;
  }
  .person__credentials { margin-top: 1px; font-size: 17.5px; font-weight: 400; }
  .divider {
    position: absolute; left: 76px; top: 194px;
    width: 530px; height: 1px; background: var(--rule);
  }
  .brand-mark {
    position: absolute; display: flex; flex-direction: column; align-items: center;
    color: var(--brand-blue); font-weight: 600; text-align: center;
  }
  .brand-mark__dot {
    border-radius: 50%; background: var(--brand-blue);
  }
  .brand-mark--front { left: 608px; top: 110px; width: 160px; font-size: 15px; line-height: 1.3; }
  .brand-mark--front .brand-mark__dot { width: 26px; height: 26px; margin-bottom: 8px; }

  .contacts { position: absolute; left: 76px; top: 298px; list-style: none; }
  .contacts__item {
    display: flex; align-items: center; gap: 8px;
    font-size: 19px; font-weight: 400; height: 25px; margin-bottom: 12px;
  }
  .contacts__item:nth-child(2) { margin-bottom: 9px; }
  .contacts__icon { width: 25px; height: 25px; flex: none; }

  .corner-accent {
    position: absolute; border-radius: 50%;
    background: radial-gradient(circle, var(--pale-blue) 0%, var(--soft-blue) 100%);
  }
  .corner-accent--front { left: 554px; top: 350px; width: 320px; height: 320px; }
  .corner-accent--back-top { left: -120px; top: -120px; width: 220px; height: 220px; }
  .corner-accent--back-bottom { left: 690px; top: 354px; width: 260px; height: 260px; }

  /* Back */
  .brand-mark--back { left: 260px; top: 60px; width: 300px; font-size: 26px; line-height: 1.25; }
  .brand-mark--back .brand-mark__dot { width: 54px; height: 54px; margin-bottom: 16px; }

  .appointment__title {
    position: absolute; left: 0; right: 0; top: 290px;
    text-align: center; font-size: 26px; letter-spacing: 8px;
    color: var(--muted); font-weight: 400; padding-left: 8px;
  }
  .appointment__title strong { font-weight: 700; }
  .appointment__field {
    position: absolute; top: 366px;
    display: flex; align-items: flex-end; gap: 6px;
    font-size: 18px; color: #333;
  }
  .appointment__field--date { left: 144px; }
  .appointment__field--time { left: 449px; }
  .appointment__line { width: 172px; height: 1px; background: #555; margin-bottom: 6px; }
</style>
</head>
<body>

<section class="card card--front">
  <div class="person">
    <h1 class="person__name"><span class="person__first">DR MARTIN</span> <span class="person__last">PELLOWE</span></h1>
    <p class="person__role">OSTEOPATH</p>
    <p class="person__credentials">(B.Clin.Sci (Ost) M.Ost BSC ECON (Hons)</p>
  </div>
  <div class="divider"></div>

  <div class="brand-mark brand-mark--front">
    <span class="brand-mark__dot"></span>
    <span>Brookfarrow Osteopathy and Dry Needling</span>
  </div>

  <ul class="contacts">
    <li class="contacts__item">
      <svg class="contacts__icon" viewBox="0 0 24 24" aria-hidden="true">
        <circle cx="12" cy="12" r="12" fill="var(--brand-blue)"/>
        <path d="M8.2 6.5l2 2.3-1.2 1.5c.8 1.8 2 3 3.8 3.8l1.5-1.2 2.3 2-1.1 1.9c-4.3-.4-7.8-3.9-8.2-8.2z" fill="#fff"/>
      </svg>
      <span>012.555.0148</span>
    </li>
    <li class="contacts__item">
      <svg class="contacts__icon" viewBox="0 0 24 24" aria-hidden="true">
        <circle cx="12" cy="12" r="12" fill="var(--brand-blue)"/>
        <path d="M12 5a4.5 4.5 0 0 0-4.5 4.5c0 3.3 4.5 8.5 4.5 8.5s4.5-5.2 4.5-8.5A4.5 4.5 0 0 0 12 5z" fill="#fff"/>
        <circle cx="12" cy="9.5" r="1.7" fill="var(--brand-blue)"/>
      </svg>
      <span>48 Lower Crane Street Brookfarrow</span>
    </li>
    <li class="contacts__item">
      <svg class="contacts__icon" viewBox="0 0 24 24" aria-hidden="true">
        <circle cx="12" cy="12" r="12" fill="var(--brand-blue)"/>
        <g fill="none" stroke="#fff" stroke-width="1.1">
          <circle cx="12" cy="12" r="6"/>
          <ellipse cx="12" cy="12" rx="2.6" ry="6"/>
          <path d="M6 12h12M7 9h10M7 15h10"/>
        </g>
      </svg>
      <span>www.brookfarrowosteosteopathy.example</span>
    </li>
  </ul>

  <div class="corner-accent corner-accent--front" role="img" aria-label="Decorative brand accent in the corner"></div>
</section>

<section class="card card--back">
  <div class="corner-accent corner-accent--back-top" role="img" aria-label="Decorative brand accent in the corner"></div>

  <div class="brand-mark brand-mark--back">
    <span class="brand-mark__dot"></span>
    <span>Brookfarrow Osteopathy and Dry Needling</span>
  </div>

  <h2 class="appointment__title">YOUR NEXT <strong>APPOINTMENT</strong></h2>
  <div class="appointment__field appointment__field--date"><span>DATE:</span><span class="appointment__line"></span></div>
  <div class="appointment__field appointment__field--time"><span>TIME:</span><span class="appointment__line"></span></div>

  <div class="corner-accent corner-accent--back-bottom" role="img" aria-label="Decorative brand accent in the corner"></div>
</section>

</body>
</html>
```